brolvix new business card design project

we need a new business card design. you can view info about us @ brolvix.example. i have attached an example of our previous card with our previous name that we no longer use. We really liked the design, colors etc. look below to see more info about this project. it asks for a limited number of words. please see our website for more info about our compnay.

Target Market(s)

law enforcement

Contact Information for Business Card

i have uploaded an example of what we used before that we liked.

Font styles to use
Serif

```html
<!DOCTYPE html>
<html lang="en">
<head>
<meta charset="utf-8">
<title>Brolvix business card</title>
<link rel="stylesheet" href="https://fonts.googleapis.com/css2?family=Josefin+Sans:wght@300&family=Open+Sans:wght@400;700&display=swap">
<style>
  :root {
    --stage: #26282c;
    --navy-deep: #0c2f44;
    --navy: #15465f;
    --navy-light: #21607f;
    --band: #1a5572;
    --paper: #ffffff;
    --ink-blue: #123f58;
    --ink-grey: #7b7f84;
    --hatch: #d9dadc;
  }
  * { box-sizing: border-box; margin: 0; padding: 0; }
  html, body { width: 1200px; height: 900px; overflow: hidden; }
  body {
    background: var(--stage);
    font-family: "Open Sans", Arial, sans-serif;
    position: relative;
  }
  .card {
    position: absolute;
    left: 320px;
    width: 560px;
    height: 320px;
    border-radius: 22px;
    overflow: hidden;
    box-shadow: 0 14px 30px rgba(0,0,0,.45);
  }
  /* front */
  .card-front { top: 60px; background: linear-gradient(160deg, var(--navy-deep) 0%, var(--navy) 55%, var(--navy-light) 100%); }
  .wordmark {
    font-family: "Josefin Sans", "Helvetica Neue", sans-serif;
    font-weight: 300;
    color: var(--paper);
    letter-spacing: 6px;
  }
  .card-front .wordmark { position: absolute; top: 74px; left: 0; width: 100%; text-align: center; font-size: 64px; }
  .front-band {
    position: absolute; left: 0; right: 0; top: 190px; height: 70px;
    background: linear-gradient(180deg, var(--navy-deep), var(--band));
    border-top: 2px solid rgba(255,255,255,.08);
  }
  .hatch-bar {
    position: absolute; left: 150px; top: 14px; width: 260px; height: 14px;
    background: repeating-linear-gradient(135deg, var(--paper) 0 3px, var(--hatch) 3px 5px);
  }
  .front-url {
    position: absolute; left: 0; width: 100%; top: 36px; text-align: center;
    color: var(--paper); font-size: 19px; letter-spacing: 1px;
  }
  /* back */
  .card-back { top: 520px; background: var(--paper); }
  .back-top {
    position: absolute; left: 0; right: 0; top: 0; height: 118px;
    background: linear-gradient(160deg, var(--navy-deep), var(--navy-light));
  }
  .card-back .wordmark { position: absolute; left: 40px; top: 36px; font-size: 50px; }
  .back-divider {
    position: absolute; left: 0; right: 0; top: 118px; height: 16px;
    background: repeating-linear-gradient(135deg, var(--paper) 0 3px, var(--hatch) 3px 5px);
    border-top: 4px solid var(--band);
  }
  .person { position: absolute; left: 40px; top: 150px; }
  .person-name { color: var(--ink-blue); font-weight: 700; font-size: 21px; }
  .person-title { color: var(--ink-grey); font-size: 13px; padding-bottom: 6px; border-bottom: 2px solid var(--ink-blue); width: 240px; }
  .contacts { position: absolute; left: 300px; top: 150px; list-style: none; }
  .contacts li { display: flex; align-items: flex-start; gap: 10px; color: var(--ink-grey); font-size: 15px; line-height: 21px; margin-bottom: 6px; }
  .contacts svg { flex: none; margin-top: 2px; }
</style>
</head>
<body>
  <section class="card card-front">
    <div class="wordmark">BROLVIX</div>
    <div class="front-band">
      <div class="hatch-bar"></div>
      <div class="front-url">www.brolvix.example</div>
    </div>
  </section>

  <section class="card card-back">
    <div class="back-top"><div class="wordmark">BROLVIX</div></div>
    <div class="back-divider"></div>
    <div class="person">
      <div class="person-name">Dana Mercer</div>
      <div class="person-title">Founder/chief Executive Officer</div>
    </div>
    <ul class="contacts">
      <li>
        <svg width="18" height="18" viewBox="0 0 18 18"><rect width="18" height="18" rx="2" fill="#15465f"/><path d="M9 3.5a3.5 3.5 0 0 0-3.5 3.5c0 2.6 3.5 7 3.5 7s3.5-4.4 3.5-7A3.5 3.5 0 0 0 9 3.5z" fill="#fff"/><circle cx="9" cy="7" r="1.3" fill="#15465f"/></svg>
        <span>1420 Alder Ridge Road<br>Springfield, TX 75001</span>
      </li>
      <li>
        <svg width="18" height="18" viewBox="0 0 18 18"><rect width="18" height="18" rx="2" fill="#15465f"/><path d="M5.5 4h2l1 3-1.3 1a7 7 0 0 0 2.8 2.8l1-1.3 3 1v2a1.5 1.5 0 0 1-1.5 1.5A8.5 8.5 0 0 1 4 5.5 1.5 1.5 0 0 1 5.5 4z" fill="#fff"/></svg>
        <span>555.014.2290</span>
      </li>
      <li>
        <svg width="18" height="18" viewBox="0 0 18 18"><rect width="18" height="18" rx="2" fill="#15465f"/><rect x="3.5" y="5" width="11" height="8" fill="#fff"/><path d="M3.5 5l5.5 4.5L14.5 5" stroke="#15465f" stroke-width="1" fill="none"/></svg>
        <span>info@brolvix.example</span>
      </li>
      <li>
        <svg width="18" height="18" viewBox="0 0 18 18"><rect width="18" height="18" rx="2" fill="#15465f"/><circle cx="9" cy="9" r="5" fill="none" stroke="#fff" stroke-width="1.3"/><path d="M4 9h10M9 4c-2 2.8-2 7.2 0 10M9 4c2 2.8 2 7.2 0 10" stroke="#fff" stroke-width="1" fill="none"/></svg>
        <span>www.brolvix.example</span>
      </li>
    </ul>
  </section>
</body>
</html>
```